Web design for a Senior Home Care company

I want a web design for a home care company called Willowmere Home Care. What WHC does is send caregivers into people's homes to assist with daily living needs such as companionship, food preparation, cleaning, bathing, using the bathroom, etc. Most of the clients are seniors. The people deciding to use WHC are usually the 50 year old children of these senior citizens. Most visitors to the site will be women searching for this service for their parents.

The call to action is to inspire the website visitors to call us to set up an appointment to meet them in their home. The site design should inspire confidence in Willowmere Home Care to care for people's needs. We want to show the same attributes that a parent should have. Safety, Security and Loving Care.

Again, the goal of the site is to inspire and make it EASY for visitors to contact us either by phone call or through the website. The first choice is that they call us.

To help you with your ideas, In the attachments I've included different versions of our logo, a site map, examples of photos we might use and very rough draft of the website copy.

Target Market(s)

The customers will mostly be seniors. But, the people who will decide to use the company will the the 50 year old children of those seniors. Also, it is mostly women who are looking for help for their parents.

Industry/Entity Type

It Company

Number of Pages Required

5+ page

Requirements
Nice to have
• I want site visitors to easily be able to contact us with a phone call or through the website. The home page should inspire people to call us.

```html
<!DOCTYPE html>
<html lang="en">
<head>
<meta charset="utf-8">
<title>Willowmere Home Care – Services</title>
<link href="https://fonts.googleapis.com/css2?family=Open+Sans:wght@400;600;700&display=swap" rel="stylesheet">
<style>
:root{
  --brand-dark:#1470b9;
  --brand-light:#29a9e1;
  --footer-bg:#1173bf;
  --nav-active:#1470b9;
  --text:#555a60;
  --rule:#d6d6d6;
  --white:#ffffff;
}
*{box-sizing:border-box;margin:0;padding:0}
html,body{width:1200px;height:2161px;overflow:hidden}
body{font-family:"Open Sans",Arial,sans-serif;color:var(--text);background:var(--white)}
.wrap{width:1044px;margin:0 auto;position:relative}

.site-header{height:110px}
.site-header .wrap{display:flex;justify-content:space-between;align-items:center;height:110px}
.brand{display:flex;align-items:center;gap:12px}
.brand-mark{width:34px;height:34px;border-radius:50%;background:var(--brand-dark)}
.brand-name{font-size:36px;font-weight:600;color:var(--brand-dark);line-height:1}
.call{display:flex;align-items:center;gap:14px}
.call-label{font-size:25px;color:var(--brand-light)}
.call-icon{width:56px;height:56px;border:2px solid var(--brand-light);border-radius:50%;display:flex;align-items:center;justify-content:center}
.call-number{font-size:34px;font-weight:700;color:var(--brand-dark)}

.main-nav{background:var(--brand-light);height:52px}
.main-nav ul{list-style:none;display:flex;height:52px}
.main-nav li{height:52px;display:flex;align-items:center;padding:0 23px;color:var(--white);font-size:18px}
.main-nav li.active{background:var(--nav-active)}

.intro{text-align:center;padding-top:52px}
.intro h1{font-size:47px;font-weight:400;color:var(--brand-dark);line-height:1.2}
.intro h1 span{color:var(--brand-light)}
.intro .tagline{font-size:21px;font-weight:700;color:var(--brand-dark);margin-top:10px}
.intro p{font-size:15.5px;line-height:25px;width:840px;margin:18px auto 0}

.services{list-style:none;margin-top:33px}
.service{display:flex;align-items:flex-start;height:200px;border-bottom:1px solid var(--rule);padding-top:0}
.service:last-child{border-bottom:none}
.service-photo{width:157px;height:157px;border-radius:50%;border:2px solid var(--brand-dark);flex:none;margin-right:18px}
.service-body{padding-top:32px}
.service h2{font-size:26px;font-weight:400;color:var(--brand-dark);line-height:1.2}
.service p{font-size:15.5px;line-height:25px;margin-top:4px;max-width:860px}
.photo-warm{background:linear-gradient(135deg,#e8cdb6,#a48a7a)}
.photo-room{background:linear-gradient(135deg,#d9c3a6,#6f7a8e)}
.photo-puzzle{background:linear-gradient(135deg,#cfa98c,#5e4a55)}
.photo-nurse{background:linear-gradient(135deg,#f3f3f3,#3b6fae)}
.photo-garden{background:linear-gradient(135deg,#6f9a52,#2f8a85)}
.closing{text-align:center;font-size:15.5px;margin-top:-9px}

.join-band{background:var(--brand-light);height:137px;margin-top:58px}
.join-band .wrap{display:flex;align-items:center;justify-content:space-between;height:137px}
.join-band p{color:var(--white);font-size:20.5px;line-height:32px}
.join-btn{background:var(--white);color:var(--brand-dark);font-weight:700;font-size:20px;width:182px;height:52px;border-radius:26px;display:flex;align-items:center;justify-content:center}

.site-footer{background:var(--footer-bg);height:468px;color:var(--white)}
.footer-cols{display:flex;padding-top:36px}
.footer-cols h3{font-size:35px;font-weight:400;line-height:1.2;margin-bottom:18px}
.contact-form{width:564px}
.field{border:1px solid var(--white);height:41px;color:var(--white);font-size:15.5px;padding:8px 8px}
.row{display:flex;gap:22px;margin-bottom:21px}
.row .field{width:228px}
.field.full{width:478px;margin-bottom:22px}
.field.message{height:82px}
.submit{background:var(--white);color:var(--footer-bg);font-weight:700;font-size:18px;width:124px;height:45px;display:flex;align-items:center;justify-content:center}
.contact-info{padding-left:0}
.info-item{display:flex;gap:12px;font-size:15.5px;line-height:25px;margin-bottom:12px}
.info-item svg{flex:none;margin-top:4px}
.info-item strong{font-weight:700}
.social{display:flex;gap:22px;margin-top:16px;margin-left:4px}
.social span{width:57px;height:57px;border-radius:50%;background:var(--brand-light)}
.social span:first-child{background:var(--white)}
.footer-bottom{border-top:1px solid rgba(255,255,255,.25);margin-top:30px;padding-top:18px;text-align:center;font-size:15.5px;color:var(--brand-light)}
.footer-bottom strong{color:var(--white)}
</style>
</head>
<body>
<header class="site-header">
  <div class="wrap">
    <div class="brand"><span class="brand-mark"></span><span class="brand-name">Willowmere Home Care</span></div>
    <div class="call">
      <span class="call-label">CALL US NOW</span>
      <span class="call-icon"><svg width="24" height="24" viewBox="0 0 24 24"><path d="M6.6 10.8a15 15 0 0 0 6.6 6.6l2.2-2.2a1 1 0 0 1 1-.25 11.4 11.4 0 0 0 3.6.6 1 1 0 0 1 1 1V20a1 1 0 0 1-1 1A17 17 0 0 1 3 4a1 1 0 0 1 1-1h3.5a1 1 0 0 1 1 1c0 1.25.2 2.45.6 3.6a1 1 0 0 1-.25 1z" fill="#29a9e1"/></svg></span>
      <span class="call-number">555-014-2270</span>
    </div>
  </div>
</header>
<nav class="main-nav">
  <ul class="wrap">
    <li class="active">HOME</li><li>ABOUT</li><li>SERVICES</li><li>FREE IN HOME CONSUTATION</li><li>CONTACT</li><li>NEWS</li><li>CLIENT PORTAL</li>
  </ul>
</nav>

<main class="wrap">
  <section class="intro">
    <h1>SERVICES <span>WE OFFER</span></h1>
    <p class="tagline">Professional. Fair. Simple. Transparent.</p>
    <p>Willowmere Home Care offers a wide variety of home care services, from once a week visits to 24-hour care. Since every situation is unique, we work together with you to create the perfect program.</p>
    <p>Here is just a short list of the services we provide.&nbsp; Don’t worry about pricing or deciphering a confusing invoice.&nbsp; All of these services are included in our simple One Flat Rate price structure.</p>
  </section>

  <ul class="services">
    <li class="service"><div class="service-photo photo-warm" role="img" aria-label="Caregiver smiling with an elderly woman"></div><div class="service-body"><h2>Companionship</h2><p>Our goal is to keep your loved one active and engaged mentally and physically in a variety of activities, as well as just being a friend. We can also do meal planning, preparation and much more.</p></div></li>
    <li class="service"><div class="service-photo photo-room" role="img" aria-label="Caregiver helping a senior man at home"></div><div class="service-body"><h2>Personal Care</h2><p>Our caretakers can offer a helping hand for dressing, bathing, or using the bathroom. We will also help with medication reminders and doses to help ensure you’re loved ones are following doctor’s orders.</p></div></li>
    <li class="service"><div class="service-photo photo-puzzle" role="img" aria-label="Senior woman and caregiver doing a jigsaw puzzle"></div><div class="service-body"><h2>Dementia &amp; Alzheimer’s Care</h2><p>Caring for a loved one suffering from dementia or Alzheimer’s can be very trying and tiring.&nbsp; Their round the clock needs can wear you down physically and mentally. Whether you need continuing help or just a break to recharge your battery, Willowmere Home Care is here for you.&nbsp; We understand the needs and our caregivers and trained to make life easier and happier for everyone.</p></div></li>
    <li class="service"><div class="service-photo photo-nurse" role="img" aria-label="Nurse assisting a senior patient"></div><div class="service-body"><h2>Housekeeping</h2><p>Having a clean living space is essential for maintaining optimal health. We clean, dust, vacuum as well as do laundry.</p></div></li>
    <li class="service"><div class="service-photo photo-garden" role="img" aria-label="Caregiver with a senior woman in a wheelchair outdoors"></div><div class="service-body"><h2>Transportation</h2><p>Let us take the wheel, driving your loved one to appointments, running errands and to other important events and activities. We can also do shopping and pick up prescriptions.</p></div></li>
  </ul>
  <p class="closing">There’s much more we can do to help.&nbsp; Please call us to schedule free in-home consultation.</p>
</main>

<section class="join-band">
  <div class="wrap">
    <p>Willowmere Home Care is always seeking enthusiastic caregivers to join our growing team.<br>If you are a professional or looking to start out, we’d love to hear from you.</p>
    <span class="join-btn">JOIN US</span>
  </div>
</section>

<footer class="site-footer">
  <div class="wrap">
    <div class="footer-cols">
      <div class="contact-form">
        <h3>GET IN TOUCH WITH US</h3>
        <div class="row"><div class="field">Enter Name</div><div class="field">Enter Contact No.</div></div>
        <div class="field full">Enter Email Id</div>
        <div class="field full message">Enter Message</div>
        <div class="submit">SUBMIT</div>
      </div>
      <div class="contact-info">
        <h3>CONTACT INFO</h3>
        <div class="info-item"><svg width="14" height="18" viewBox="0 0 14 18"><path d="M7 0a7 7 0 0 0-7 7c0 5 7 11 7 11s7-6 7-11a7 7 0 0 0-7-7zm0 9.5A2.5 2.5 0 1 1 7 4.5a2.5 2.5 0 0 1 0 5z" fill="#fff"/></svg><span>Lorem Ipsum is simply dummy<br>text of the printing.</span></div>
        <div class="info-item"><svg width="18" height="18" viewBox="0 0 24 24"><path d="M6.6 10.8a15 15 0 0 0 6.6 6.6l2.2-2.2a1 1 0 0 1 1-.25 11.4 11.4 0 0 0 3.6.6 1 1 0 0 1 1 1V20a1 1 0 0 1-1 1A17 17 0 0 1 3 4a1 1 0 0 1 1-1h3.5a1 1 0 0 1 1 1c0 1.25.2 2.45.6 3.6a1 1 0 0 1-.25 1z" fill="#fff"/></svg><strong>555 018 3364</strong></div>
        <div class="info-item"><svg width="18" height="14" viewBox="0 0 18 14"><rect x="1" y="1" width="16" height="12" rx="1.5" fill="none" stroke="#fff" stroke-width="1.6"/><path d="M1.5 2l7.5 6 7.5-6" fill="none" stroke="#fff" stroke-width="1.6"/></svg><span>info@willowmerehomecare.com</span></div>
        <div class="social"><span></span><span></span><span></span></div>
      </div>
    </div>
    <div class="footer-bottom">© <strong>WILLOWMERE HOME CARE</strong> - 2016. All Rights Reserved.</div>
  </div>
</footer>
</body>
</html>
```